Creation of a Nutrition Consulting Flyer. For more information please see attached word document.

Industry/Entity Type

Health Service

Requirements
Must have
• Contend please see word document
The 3 fold flyer must meet the requirements of the DL formats, which is 210mm x 99 mm or for non 3 fold flyers DIN A 5 which is 210 mm x 148 mm (folded or non folded).
Nice to have
• our current idea is a 3 fold flyer but i am more than happy to receive other formats that better present the contend provided.

```html
<!DOCTYPE html>
<html lang="en">
<head>
<meta charset="utf-8">
<title>Esskultur.blog – Nutrition Consulting Flyer</title>
<link rel="stylesheet" href="https://fonts.googleapis.com/css2?family=Open+Sans:wght@300;400;600;700&family=Source+Sans+3:wght@400;600&display=swap">
<style>
  :root{
    --stage:#5c5c5c;
    --paper:#ffffff;
    --ink:#1d1d1d;
    --ink-soft:#3a3a3a;
    --teal-band:#a9d0ca;
    --teal-dark:#2f5f5b;
    --black-band:#111111;
    --rule:#222222;
    --greens-1:#9fbf7a;
    --greens-2:#dfe8cf;
    --lemon:#f4eec4;
  }
  *{box-sizing:border-box;margin:0;padding:0}
  html,body{width:1200px;height:900px;overflow:hidden}
  body{background:var(--stage);font-family:"Source Sans 3",Arial,sans-serif;color:var(--ink);position:relative}

  .panel{position:absolute;top:90px;width:376px;height:720px;background:var(--paper);overflow:hidden}
  .cover{left:24px}
  .inside-left{left:424px}
  .inside-right{left:800px}

  /* ---------- Cover ---------- */
  .cover-backdrop{position:absolute;inset:0 0 137px 0;
    background:radial-gradient(circle at 75% 12%,var(--lemon) 0,rgba(244,238,196,0) 40%),
               linear-gradient(180deg,#e9eee3 0%,#f7f7f3 45%,#ececea 100%)}
  .brand-title{position:absolute;top:52px;left:0;right:0;text-align:center;
    font-family:"Open Sans",Arial,sans-serif;font-weight:300;font-size:37px;letter-spacing:.5px;color:var(--ink)}
  .cover .title-rule{position:absolute;top:110px;left:38px;right:38px;height:1.5px;background:var(--rule)}
  .brand-author{position:absolute;top:120px;left:0;right:0;text-align:center;
    font-family:"Open Sans",Arial,sans-serif;font-size:19px;color:var(--ink)}
  .cover-dish{position:absolute;top:168px;left:22px;width:340px;height:340px;border-radius:50%;
    background:radial-gradient(circle at 48% 50%,#7e9a48 0,#5f8a35 30%,#b9d3c8 58%,#dfe9e6 72%,#f4f5f3 100%)}
  .tagline-band{position:absolute;left:0;right:0;top:583px;height:61px;background:var(--teal-band);
    display:flex;align-items:center;justify-content:center;
    font-family:"Open Sans",Arial,sans-serif;font-size:18.5px;color:var(--ink)}
  .web-band{position:absolute;left:0;right:0;bottom:0;height:76px;background:var(--black-band);
    display:flex;align-items:center;justify-content:center;
    color:#fff;font-size:12px;letter-spacing:4px}

  /* ---------- Inside left ---------- */
  .inside-left .header-photo{position:absolute;top:0;left:0;right:0;height:150px;
    background:linear-gradient(180deg,var(--greens-1) 0%,var(--greens-2) 55%,rgba(255,255,255,0) 100%)}
  .inside-left .page-tint{position:absolute;inset:0;background:linear-gradient(180deg,#f6f7f1,#fafaf8 60%,#eef3e6)}
  .inside-left .brand-title{top:105px;font-size:30px}
  .inside-left .brand-author{top:150px;font-size:17px}
  .motto-box{position:absolute;top:195px;left:0;width:318px;padding:12px 20px;background:var(--black-band);
    color:#fff;font-family:"Open Sans",Arial,sans-serif}
  .motto-box .lead{font-size:20px;line-height:1.2}
  .motto-box .rest{font-size:15px;line-height:1.3}
  .advise{position:absolute;top:300px;left:24px;right:24px}
  .advise .dots{height:0;border-top:2px dotted var(--teal-dark)}
  .advise h2{font-family:"Open Sans",Arial,sans-serif;font-weight:600;font-size:22px;color:var(--teal-dark);
    padding:6px 0 4px;letter-spacing:.5px}
  .topic-list{position:absolute;top:372px;left:24px;right:20px;display:grid;grid-template-columns:1fr 1fr;gap:10px 14px;list-style:none}
  .topic-list li{position:relative;padding-left:14px;font-size:11px;line-height:1.3;color:var(--ink-soft)}
  .topic-list li::before{content:"";position:absolute;left:0;top:4px;width:7px;height:7px;background:var(--teal-dark)}
  .dish-circles{position:absolute;top:478px;left:24px;display:flex;gap:10px}
  .dish-circle{width:100px;height:100px;border-radius:50%;border:3px solid #fff}
  .dish-circle.smoothie{background:radial-gradient(circle,#8aa23a,#3b5a2c)}
  .dish-circle.salad{background:radial-gradient(circle,#d9a34a,#a9c27a 60%,#e9ecea)}
  .dish-circle.bowl{background:radial-gradient(circle,#c96c3f,#7fa05a 55%,#e4e8e2)}
  .lettuce-footer{position:absolute;left:0;right:0;bottom:0;height:150px;
    background:linear-gradient(180deg,rgba(255,255,255,0),rgba(190,214,150,.55))}

  /* ---------- Inside right ---------- */
  .inside-right .lettuce-footer{height:130px}
  .portrait-frame{position:absolute;top:52px;left:10px;width:158px;height:508px;border:1.5px solid var(--rule);padding:5px}
  .portrait-photo{width:100%;height:100%;background:linear-gradient(180deg,#d8d6d0 0%,#ecebe6 40%,#f2f1ee 70%,#3b4150 100%)}
  .bio{position:absolute;top:52px;left:178px;right:12px}
  .bio h1{font-family:"Open Sans",Arial,sans-serif;font-weight:600;font-size:20px;text-align:center;letter-spacing:.3px}
  .bio .role{font-size:9.5px;text-align:center;margin-top:4px;padding-bottom:4px;border-bottom:2px dashed var(--rule);
    width:120px;margin-left:auto;margin-right:auto}
  .bio p{font-size:8.6px;line-height:1.32;text-align:justify;margin-top:9px;color:var(--ink-soft)}
  .bio .divider{width:40px;height:2px;background:var(--rule);margin:10px auto 0}
</style>
</head>
<body>

  <!-- Front cover -->
  <section class="panel cover">
    <div class="cover-backdrop" role="img" aria-label="Soft background photo of lemons and fresh greens"></div>
    <div class="brand-title">ESSKULTUR.BLOG</div>
    <div class="title-rule"></div>
    <div class="brand-author">Dr. Lena Markwald</div>
    <div class="cover-dish" role="img" aria-label="Photo of a plate with spinach, tomato and avocado salad"></div>
    <div class="tagline-band">WELLBEING – LIFE QUALITY – HEALTH</div>
    <div class="web-band">www.esskultur.blog</div>
  </section>

  <!-- Inside left panel -->
  <section class="panel inside-left">
    <div class="page-tint"></div>
    <div class="header-photo" role="img" aria-label="Photo of lettuce, lemons and blueberries"></div>
    <div class="brand-title">ESSKULTUR.BLOG</div>
    <div class="brand-author">Dr. Lena Markwald</div>
    <div class="motto-box">
      <div class="lead">Improving quality of live based</div>
      <div class="rest">on nutrition is my Motto</div>
    </div>
    <div class="advise">
      <div class="dots"></div>
      <h2>I ADVISE YOU ON</h2>
      <div class="dots"></div>
    </div>
    <ul class="topic-list">
      <li>Healthy weight diet</li>
      <li>Nutrition during nursing</li>
      <li>Nutrition in pregnancy</li>
      <li>Preparation of beneficial dishes for the whole family</li>
      <li>Food allergies</li>
      <li>Intestinal health</li>
    </ul>
    <div class="dish-circles">
      <div class="dish-circle smoothie" role="img" aria-label="Photo of a green smoothie in a jar"></div>
      <div class="dish-circle salad" role="img" aria-label="Photo of a fresh salad plate"></div>
      <div class="dish-circle bowl" role="img" aria-label="Photo of a vegetable pasta bowl"></div>
    </div>
    <div class="lettuce-footer" role="img" aria-label="Faded photo of lettuce leaves"></div>
  </section>

  <!-- Inside right panel -->
  <section class="panel inside-right">
    <div class="lettuce-footer" role="img" aria-label="Faded photo of lettuce leaves"></div>
    <div class="portrait-frame">
      <div class="portrait-photo" role="img" aria-label="Portrait photo of the nutritionist holding a bowl of strawberries"></div>
    </div>
    <div class="bio">
      <h1>DR. LENA MARKWALD</h1>
      <div class="role">Diplom-Ökotrophologin</div>
      <p>Starting at my childhood, nutrition started to play a major role in my life.</p>
      <p>I was fascinated, on how much potential our daily life food has on our health. This knowledge I have gained during my career is what I would like to pass on to as many people as possible to profit from the enormous profits of a healthy diet.</p>
      <div class="divider"></div>
      <p>My aim is, to perfectly support you to achieve your aims.</p>
      <p>I offer personal as well as online coaching. We could meet at your place, in a café, at my place or online via multiple channels. As your personal coach I will be available to answer your questions or solve your questions in a responsible and binding manner.</p>
      <p>One of the most effective ways you can take to improve your health is to increase your energy level and to prevent chronical diseases, is to alter to a healthy and nutrition diet.</p>
      <p>Whenever there is a desire to change the current condition, coaching can support you on boost this desire for a change to the better. Using suitable questions and tools, we will define your aims and define measures to achieve your goals. You will understand, on what can be changed in your nutrition in order to make the change sustainable. My holistic nutrition coaching is fully tailored to your needs and circumstances. You are the one determining on what shall be done and in which speed. And with my consultation, I am positive that you will master your challenge.</p>
    </div>
  </section>

</body>
</html>
```